Zielgruppe
Planung und Realisierung von individuellen und wertbeständigen Kamin- und Ofenlösungen, sowie Fliesen- und Baddesign.
Aufgabenstellung
Wir benötigen ein möglichst schlichtes Design für Visitenkarten, bzw. Briefpapier. Für die Visitenkarten gerne auch Vorschläge mit Prägung, Ausstanzung oder mit Heißfolie. Auch Klappkarten wären denkbar. Das Design soll "das gewisse Etwas haben" und nicht zu verspielt sein.
Die Visitenkarten sind für die Firma KARMU, das Logo von der Ausstellung "talgrund" soll dezent mit eingebunden werden (bei dem Briefpapier z.B. in der Fußzeile". Die farbliche Gestaltung sollte sich an den Farben des Logos orientieren.
Schriftart für Texte: Century Gothic
Schriftfarbe: RAL 7016
Nur eine Idee: Ich könnte mir auch gut vorstellen, dass die Visitenkarte aus einer Zündholzverpackung (wenn dann aber eine besondere mit nur einem Zündholz oder einem besonders breiten) besteht: http://lindoraversand.de/produkte_briefchen.php

```html
<!DOCTYPE html>
<html lang="de">
<head>
<meta charset="utf-8">
<title>KARMU – Briefpapier und Visitenkarte</title>
<link href="https://fonts.googleapis.com/css2?family=Questrial&display=swap" rel="stylesheet">
<style>
  :root {
    --board: #c99e69;
    --anthracite: #263439;
    --orange: #f08500;
    --paper: #ffffff;
    --text: #293133;
    --light: #e3e6e7;
    --muted: #9aa3a6;
  }
  html, body { margin: 0; padding: 0; overflow: hidden; }
  body { width: 1200px; height: 1120px; background: var(--board); font-family: "Questrial", sans-serif; color: var(--text); }
  .board { position: relative; width: 1200px; height: 1120px; }
  .abs { position: absolute; }

  /* Letterhead */
  .letterhead { left: 52px; top: 42px; width: 730px; height: 1032px; background: var(--paper); box-shadow: 4px 5px 8px rgba(0,0,0,.25); }
  .letterhead__topline { left: 0; top: 0; width: 100%; height: 12px; background: var(--orange); }
  .letterhead__header { left: 0; top: 12px; width: 100%; height: 95px; background: var(--anthracite); }
  .brand-name { font-size: 52px; letter-spacing: 2px; line-height: 1; }
  .letterhead .brand-name { right: 30px; top: 20px; color: var(--light); }
  .letterhead .brand-tagline { right: 31px; top: 78px; font-size: 15px; color: var(--light); }
  .contact-block { left: 547px; top: 136px; font-size: 14px; line-height: 16.5px; }
  .contact-block .spaced { letter-spacing: 1.5px; }
  .contact-block .gap { margin-top: 4px; }
  .exhibition-mark { right: 35px; top: 243px; font-size: 11px; }
  .sender-line { left: 93px; top: 184px; font-size: 8px; letter-spacing: 1px; display: flex; align-items: center; gap: 5px; }
  .sender-line__dot { width: 5px; height: 5px; background: var(--orange); }
  .mark-square { width: 4px; height: 4px; background: var(--orange); }
  .fold-mark { left: 0; width: 0; height: 0; border-top: 7px solid transparent; border-bottom: 7px solid transparent; border-left: 7px solid var(--orange); }
  .letterhead__footline { left: 0; top: 923px; width: 100%; height: 13px; background: var(--orange); }
  .letterhead__footer { left: 0; top: 936px; width: 100%; height: 96px; background: var(--anthracite); color: var(--light); }
  .footer-company { left: 31px; top: 21px; font-size: 9px; line-height: 12.5px; }
  .footer-company .company { font-size: 11px; }
  .footer-bank { right: 25px; top: 13px; font-size: 8.5px; line-height: 13px; text-align: right; }

  /* Business card */
  .card { width: 334px; height: 216px; box-shadow: 5px 6px 9px rgba(0,0,0,.3); }
  .card--front { left: 827px; top: 304px; background: var(--paper); }
  .card__edge { right: 0; top: 0; width: 10px; height: 100%; background: var(--orange); }
  .card--front .brand-name { left: 10px; top: 14px; font-size: 38px; color: #111; }
  .card--front .brand-tagline { left: 10px; top: 51px; font-size: 12px; color: var(--text); }
  .card__accent { left: 185px; top: 92px; width: 9px; height: 30px; background: var(--orange); }
  .card__person { right: 21px; top: 95px; text-align: right; }
  .card__name { font-size: 18px; line-height: 20px; }
  .card__role { font-size: 8.5px; }
  .card__address { left: 19px; top: 143px; font-size: 11px; line-height: 13.5px; }
  .card__address .gap { margin-top: 2px; }
  .card__web { right: 21px; top: 198px; font-size: 11px; }
  .card--back { left: 827px; top: 559px; background: var(--anthracite); }
  .card--back .brand-name { left: 0; width: 100%; top: 84px; text-align: center; color: var(--orange); font-size: 44px; }
  .card__exhibition { right: 11px; top: 190px; text-align: right; color: var(--muted); font-size: 12px; line-height: 11px; }
  .card__exhibition small { display: block; font-size: 4px; line-height: 5px; }
</style>
</head>
<body>
<div class="board">

  <section class="letterhead abs" aria-label="Briefpapier">
    <div class="letterhead__topline abs"></div>
    <header class="letterhead__header abs">
      <div class="brand-name abs">KARMU</div>
      <div class="brand-tagline abs">kamine · öfen · fliesen</div>
    </header>

    <div class="sender-line abs"><span class="sender-line__dot"></span>KARMU GmbH &nbsp;|&nbsp; Am Talweg 12 &nbsp;|&nbsp; 34512 Lindenau</div>

    <address class="contact-block abs" style="font-style:normal">
      <div class="spaced">Am Talweg 12</div>
      <div class="spaced">34512 Lindenau</div>
      <div>fon:&nbsp;&nbsp; 05642 / 71 38 20</div>
      <div>fax:&nbsp;&nbsp;&nbsp; 05642 / 71 38 29</div>
      <div class="gap">info@karmu-lindenau.de</div>
      <div>www.karmu-lindenau.de</div>
    </address>
    <div class="exhibition-mark abs">talgrund</div>

    <div class="mark-square abs" style="left:72px;top:455px"></div>
    <div class="mark-square abs" style="left:365px;top:455px"></div>
    <div class="fold-mark abs" style="top:357px"></div>
    <div class="fold-mark abs" style="top:722px"></div>

    <div class="letterhead__footline abs"></div>
    <footer class="letterhead__footer abs">
      <div class="footer-company abs">
        <div class="company">KARMU GmbH</div>
        <div>Geschäftsführer: Erik Sommer</div>
        <div>Amtsgericht Lindenau: 1 HRB 555</div>
        <div>Ust-ID.Nr.: DE 987654321</div>
        <div>Steuernummer: 035 544 12345</div>
      </div>
      <div class="footer-bank abs">
        <div>Bankverbindung 1:</div>
        <div>BIC: GENODEF1LIN</div>
        <div>IBAN: DE12 30460 0007 0000 0318 26</div>
        <div>Bankverbindung 2:</div>
        <div>BIC: GENODEF1LIN</div>
        <div>IBAN: DE12 30460 0007 0000 0318 26</div>
      </div>
    </footer>
  </section>

  <section class="card card--front abs" aria-label="Visitenkarte Vorderseite">
    <div class="brand-name abs">KARMU</div>
    <div class="brand-tagline abs">kamine · öfen · fliesen</div>
    <div class="card__accent abs"></div>
    <div class="card__person abs">
      <div class="card__name">Lukas Brenner</div>
      <div class="card__role">Geschäftsführer</div>
    </div>
    <address class="card__address abs" style="font-style:normal">
      <div>Am Talweg 12</div>
      <div>34512 Lindenau</div>
      <div>fon:&nbsp; 05642 / 71 38 20</div>
      <div>fax:&nbsp; 05642 / 71 38 29</div>
      <div class="gap">info@karmu-lindenau.de</div>
    </address>
    <div class="card__web abs">www.karmu-lindenau.de</div>
    <div class="card__edge abs"></div>
  </section>

  <section class="card card--back abs" aria-label="Visitenkarte Rückseite">
    <div class="brand-name abs">KARMU</div>
    <div class="card__exhibition abs">talgrund<small>bad raum leben</small></div>
  </section>

</div>
</body>
</html>
```